Indian Takeaway Menu

We need a flyer for an existing Indian Takeaway business in dublin Ireland.

We need some upto date style menu may be a A4 sheet folded in 3 layers.

But not folded in landscape side folded from portrait side and typing from portrait side from top, as we type in a word document and then fold the letter in 3 layers.
please amend your designs as everyone have done the same thing which is very boring.

We have a logo we would like to use in front of the menu. Designer have to come up with the colour which will help the logo to stand out. we also have a review in the paper which we would like to use at the back page somewhere.

New ideas are welcome from the designer
Please look at the example menu attached.

Target Market(s)

City population

Industry/Entity Type

Landscape

Font styles to use
Sans Serif

Colors
acd037

Requirements
Must have
• ingredient sign for
• Nuts
• Celiac
• Low fat
• Diary
Nice to have
• attractive

```html
<!DOCTYPE html>
<html lang="en">
<head>
<meta charset="utf-8">
<title>Saffron Hearth – Takeaway Menu</title>
<link href="https://fonts.googleapis.com/css2?family=Jost:ital,wght@0,400;0,600;0,700;1,400&display=swap" rel="stylesheet">
<style>
  :root{
    --paper:#fcf5a6;
    --ink:#1c1c1c;
    --soft:#333;
    --badge-line:#222;
    --emblem:#6e6350;
    --chilli-red:#c2372a;
    --chilli-amber:#d98a1c;
    --chilli-green:#4f7a2a;
  }
  *{box-sizing:border-box;margin:0;padding:0}
  html,body{width:848px;height:1200px;overflow:hidden;background:var(--paper)}
  body{position:relative;font-family:'Jost',sans-serif;color:var(--ink)}
  .menu-section{position:absolute}
  .col-a{left:53px;width:236px}
  .col-b{left:311px;width:216px}
  .col-c{left:560px;width:234px}

  .section-title{font-weight:400;font-size:18.5px;line-height:20px;letter-spacing:-.1px;display:flex;align-items:center;gap:14px;margin-bottom:14px}
  .section-title .emblem{width:26px;height:20px;border-radius:4px;background:var(--emblem);flex:none}
  .section-title.two-line{font-size:16.5px;line-height:20px}

  .dish{margin-bottom:var(--gap,13px)}
  .dish-row{display:flex;align-items:center;justify-content:space-between}
  .dish-name{font-weight:700;font-size:9.6px;letter-spacing:.1px;text-transform:uppercase;display:flex;align-items:center;gap:5px}
  .price{font-size:10px;font-weight:400}
  .dish-desc{font-style:italic;font-size:7.8px;line-height:11px;color:var(--soft);margin-top:3px;padding-right:8px}

  .badge{display:inline-flex;align-items:center;justify-content:center;min-width:12px;height:13px;padding:0 2px;border:1px solid var(--badge-line);border-radius:3px;font-size:7.5px;font-weight:600;line-height:1}
  .chilli{display:inline-block;width:15px;height:7px;border-radius:7px 7px 4px 4px}
  .chilli.red{background:var(--chilli-red)}
  .chilli.amber{background:var(--chilli-amber)}
  .chilli.green{background:var(--chilli-green)}

  .side-list .dish{margin-bottom:0;height:17.3px}
  .side-list .dish-name{font-size:9.6px}
</style>
</head>
<body>

<!-- Column A -->
<section class="menu-section col-a" style="top:58px">
  <h2 class="section-title">Vegetarian Starters <span class="emblem" role="img" aria-label="elephant emblem"></span></h2>
  <div class="dish" style="--gap:14px"><div class="dish-row"><span class="dish-name">Onion Bhajia</span><span class="price">€4.00</span></div><p class="dish-desc">Sliced onions, fresh spinach and herbs fried with gram flour until golden.</p></div>
  <div class="dish" style="--gap:14px"><div class="dish-row"><span class="dish-name">Vegetable Samosa <span class="badge">CL</span></span><span class="price">€4.00</span></div><p class="dish-desc">Crispy handmade pastry filled with potato and peas deep fried with herb until golden.</p></div>
  <div class="dish" style="--gap:14px"><div class="dish-row"><span class="dish-name">Palak Kachori <span class="chilli amber" role="img" aria-label="mild chilli"></span></span><span class="price">€4.00</span></div><p class="dish-desc">Golden fried cakes of fresh spinach and yellow chana lentil, served with tamarind dip. (Recommended)</p></div>
  <div class="dish" style="--gap:14px"><div class="dish-row"><span class="dish-name">Vegetable Pakora</span><span class="price">€4.00</span></div><p class="dish-desc">Cauliflower, potato and onion golden fried with gram flour batter.</p></div>
  <div class="dish"><div class="dish-row"><span class="dish-name">Aloo Channa Chaat <span class="badge">LF</span></span><span class="price">€3.50</span></div><p class="dish-desc">Aloo channa chaat is a low fat snack made with boiled chickpeas, potatoes and chaat masala.</p></div>
</section>

<section class="menu-section col-a" style="top:428px">
  <h2 class="section-title">Chicken Dishes <span class="emblem" role="img" aria-label="elephant emblem" style="margin-left:34px"></span></h2>
  <div class="dish" style="--gap:15px"><div class="dish-row"><span class="dish-name">Chicken Dansak</span><span class="price">€8.50</span></div><p class="dish-desc">Sweet and sour sauce prepared with mixed fruit and spices.</p></div>
  <div class="dish" style="--gap:14px"><div class="dish-row"><span class="dish-name">Chicken Saag <span class="badge">D</span><span class="badge">LF</span></span><span class="price">€9.50</span></div><p class="dish-desc">Chicken breast pieces cooked with spinach, fresh herbs, tomato tangy sauce and coriander</p></div>
  <div class="dish" style="--gap:14px"><div class="dish-row"><span class="dish-name">Chicken Royale Korma <span class="badge">D</span></span><span class="price">€8.50</span></div><p class="dish-desc">Chopped breast of chicken cooked in a rich creamy sauce with coconut, probably most popular amongst the Irish.</p></div>
  <div class="dish" style="--gap:14px"><div class="dish-row"><span class="dish-name">Saffron Hearth Chicken Curry <span class="badge">D</span><span class="badge">N</span></span><span class="price">€8.50</span></div><p class="dish-desc">Traditional Indian chicken curry to suit most palates mild, medium or hot, you choose.</p></div>
  <div class="dish" style="--gap:14px"><div class="dish-row"><span class="dish-name">Chicken Karahi <span class="badge">LF</span></span><span class="price">€8.00</span></div><p class="dish-desc">Diced chicken prepared with green peppers, spring onions, tomatoes and whole Indian spices.</p></div>
  <div class="dish"><div class="dish-row"><span class="dish-name">Chicken Tikka Masala <span class="badge">D</span><span class="badge">LF</span></span><span class="price">€8.00</span></div><p class="dish-desc">Tender chicken tikka cooked in a smooth creamy tomato sauce. Most popular.</p></div>
</section>

<section class="menu-section col-a" style="top:827px">
  <div class="dish" style="--gap:14px"><div class="dish-row"><span class="dish-name">South-Indian Garlic Chilli <span class="chilli red" role="img" aria-label="hot chilli"></span><span class="badge">D</span><span class="badge">LF</span></span><span class="price">€8.00</span></div><p class="dish-desc">Tasty red chicken curry loaded with garlic, ground spices, fresh herbs and green chillies.</p></div>
  <div class="dish" style="--gap:14px"><div class="dish-row"><span class="dish-name">Chicken Dahiwala <span class="chilli red" role="img" aria-label="hot chilli"></span><span class="badge">D</span></span><span class="price">€8.00</span></div><p class="dish-desc">Amazingly spicy chicken curry with fresh coconut, yoghurt, green chillies, ginger and herbs.</p></div>
  <div class="dish" style="--gap:14px"><div class="dish-row"><span class="dish-name">Chicken Vegetable &amp; Nut Curry <span class="badge">D</span><span class="badge">N</span></span><span class="price">€8.50</span></div><p class="dish-desc">Boneless chicken breast pieces sautéed with fresh vegetables, nuts and herbs in a smooth and creamy sauce.</p></div>
  <div class="dish"><div class="dish-row"><span class="dish-name">Chicken Biryani <span class="chilli amber" role="img" aria-label="mild chilli"></span><span class="badge">N</span></span><span class="price">€9.00</span></div><p class="dish-desc">Breast of chicken chopped and cooked with Basmati rice, fresh herbs, spices and fried onions accompanied with vegetable curry.</p></div>
</section>

<!-- Column B -->
<section class="menu-section col-b" style="top:58px">
  <h2 class="section-title">Meat Starters <span class="emblem" role="img" aria-label="elephant emblem" style="margin-left:20px"></span></h2>
  <div class="dish" style="--gap:12px"><div class="dish-row"><span class="dish-name">Keema Singhara <span class="badge">N</span><span class="badge">CL</span></span><span class="price">€4.00</span></div><p class="dish-desc">Crispy handmade pastry filled with lamb mince, fresh herbs and spices accompanied with a tongue tingling mint chutney.</p></div>
  <div class="dish" style="--gap:12px"><div class="dish-row"><span class="dish-name">Prawn Chatpate</span><span class="price">€5.00</span></div><p class="dish-desc">Pan-fried prawns cooked with tangy lemon and coriander sauce</p></div>
  <div class="dish" style="--gap:12px"><div class="dish-row"><span class="dish-name">Chicken Tikka <span class="badge">D</span></span><span class="price">€4.50</span></div><p class="dish-desc">Tender pieces of chicken marinated, cooked in a clay oven and served with salad and a Mint dip.</p></div>
  <div class="dish" style="--gap:12px"><div class="dish-row"><span class="dish-name">Seekh Kebab</span><span class="price">€5.00</span></div><p class="dish-desc">A lamb mince barbecued delicacy, served with salad and a mint dip</p></div>
  <div class="dish" style="--gap:18px"><div class="dish-row"><span class="dish-name">Chicken Pakora</span><span class="price">€5.00</span></div><p class="dish-desc">Boneless pieces of chicken coated in batter/spice, deep fried.</p></div>
  <div class="dish"><div class="dish-row"><span class="dish-name">Chicken Wings</span><span class="price">€5.00</span></div></div>
</section>

<section class="menu-section col-b" style="top:424px">
  <h2 class="section-title">Lamb Dishes <span class="emblem" role="img" aria-label="elephant emblem" style="margin-left:20px"></span></h2>
  <div class="dish" style="--gap:8px"><div class="dish-row"><span class="dish-name">Lamb Bhuna <span class="chilli amber" role="img" aria-label="mild chilli"></span></span><span class="price">€9.50</span></div><p class="dish-desc">Spring lamb pieces sautéed with spring onions, tomatoes, crushed black pepper and fresh herbs</p></div>
  <div class="dish" style="--gap:8px"><div class="dish-row"><span class="dish-name">Haandi Gosht <span class="chilli amber" role="img" aria-label="mild chilli"></span></span><span class="price">€9.50</span></div><p class="dish-desc">Lamb cooked with chunky pepper, onions, tomatoes, mushrooms, green chilli and fresh coriander</p></div>
  <div class="dish" style="--gap:10px"><div class="dish-row"><span class="dish-name">Palak Gosht <span class="badge">D</span></span><span class="price">€9.50</span></div><p class="dish-desc">Pan-fried lamb pieces cooked with spinach, fresh herbs and coriander</p></div>
  <div class="dish" style="--gap:8px"><div class="dish-row"><span class="dish-name">Lamb Roganjosh <span class="chilli red" role="img" aria-label="hot chilli"></span></span><span class="price">€9.50</span></div><p class="dish-desc">A red lamb curry prepared with fresh herbs and spices, a delicacy from Kashmir.</p></div>
  <div class="dish" style="--gap:8px"><div class="dish-row"><span class="dish-name">Lamb Kohlapuri <span class="chilli red" role="img" aria-label="hot chilli"></span><span class="badge">D</span><span class="badge">N</span></span><span class="price">€10.00</span></div><p class="dish-desc">A hot lamb dish from the southern coast of India, flavoured with yoghurt nuts and coconut.</p></div>
  <div class="dish" style="--gap:8px"><div class="dish-row"><span class="dish-name">Lamb Jalfrezi <span class="chilli amber" role="img" aria-label="mild chilli"></span><span class="badge">D</span><span class="badge">N</span></span><span class="price">€10.00</span></div><p class="dish-desc">Lamb tossed with strips of onions, assorted bell peppers flavoured with crushed coriander seeds and dry fenugreek.</p></div>
  <div class="dish"><div class="dish-row"><span class="dish-name">Gosht Biryani Sofyani <span class="chilli amber" role="img" aria-label="mild chilli"></span><span class="badge">N</span></span><span class="price">€10.50</span></div><p class="dish-desc">Basmati rice cooked with lamb, ginger and garlic accompanied with vegetable curry or raita.</p></div>
</section>

<section class="menu-section col-b" style="top:800px">
  <h2 class="section-title">Prawn Dishes <span class="emblem" role="img" aria-label="elephant emblem" style="margin-left:22px"></span></h2>
  <div class="dish" style="--gap:12px"><div class="dish-row"><span class="dish-name">Tandoori Prawn Masala <span class="chilli green" role="img" aria-label="green chilli"></span><span class="badge">D</span><span class="badge">N</span></span><span class="price">€10.00</span></div><p class="dish-desc">Sautéed prawns in a smooth creamy sauce flavoured with kasoori methi and tandoori spices</p></div>
  <div class="dish" style="--gap:12px"><div class="dish-row"><span class="dish-name">Prawn Karahi <span class="chilli amber" role="img" aria-label="mild chilli"></span><span class="badge">LF</span></span><span class="price">€10.00</span></div><p class="dish-desc">Succulent prawns cooked with green peppers, spring onions, tomatoes &amp; whole spices</p></div>
  <div class="dish" style="--gap:12px"><div class="dish-row"><span class="dish-name">Prawn Bhuna <span class="badge">LF</span></span><span class="price">€10.00</span></div><p class="dish-desc">Prawns cooked in a tomato and onion sauce with crushed black pepper and spring onions</p></div>
  <div class="dish" style="--gap:16px"><div class="dish-row"><span class="dish-name">Goan Prawn Curry <span class="chilli red" role="img" aria-label="hot chilli"></span><span class="badge">D</span><span class="badge">N</span></span><span class="price">€10.50</span></div><p class="dish-desc">Fisherman's favourite prawn curry flavoured with curry leaves, coconut, crushed spices &amp; fresh herbs</p></div>
  <div class="dish"><div class="dish-row"><span class="dish-name">Prawn Biryani</span><span class="price">€10.00</span></div><p class="dish-desc">Shrimp prawn cooked with eggs, green peas and onion.</p></div>
</section>

<!-- Column C -->
<section class="menu-section col-c" style="top:50px">
  <h2 class="section-title two-line">Clay Oven Dishes Served with Naan &amp; Curry Sauce</h2>
  <div class="dish" style="--gap:14px"><div class="dish-row"><span class="dish-name">Tandoori Chicken (Half) <span class="badge">D</span></span><span class="price">€9.50</span></div><p class="dish-desc">Spring chicken marinated with yoghurt and tandoori spices, grilled in clay oven</p></div>
  <div class="dish" style="--gap:14px"><div class="dish-row"><span class="dish-name">Chicken Tikka <span class="badge">D</span></span><span class="price">€9.50</span></div><p class="dish-desc">Tender breast pieces of chicken marinated and cooked in a clay oven</p></div>
  <div class="dish" style="--gap:12px"><div class="dish-row"><span class="dish-name">Seekh Kebab</span><span class="price">€10.00</span></div><p class="dish-desc">A lamb mince barbecued delicacy</p></div>
  <div class="dish"><div class="dish-row"><span class="dish-name">Saffron Hearth's Mix Grill <span class="badge">D</span></span><span class="price">€10.50</span></div><p class="dish-desc">2 pcs of chicken tikka, 2 pcs seekh kebab, 2 pcs battered prawns, 1 pc tandoori chicken</p></div>
</section>

<section class="menu-section col-c" style="top:293px">
  <h2 class="section-title">Vegetarian Dishes <span class="emblem" role="img" aria-label="elephant emblem"></span></h2>
  <div class="dish" style="--gap:16px"><div class="dish-row"><span class="dish-name">Gajjar Mattar Paneer <span class="badge">D</span><span class="badge">N</span></span><span class="price">€8.00</span></div><p class="dish-desc">chopped carrots, peas and Indian cheese in a semi-dry sauce. Recommended</p></div>
  <div class="dish" style="--gap:38px"><div class="dish-row"><span class="dish-name">Dhingri Dulma <span class="chilli green" role="img" aria-label="green chilli"></span><span class="badge">D</span><span class="badge">N</span></span><span class="price">€8.00</span></div><p class="dish-desc">Fresh mushrooms and Indian cheese in a creamy sauce.</p></div>
  <div class="dish" style="--gap:14px"><div class="dish-row"><span class="dish-name">Dum Wale Aloo</span><span class="price">€7.70</span></div><p class="dish-desc">Potatoes cooked with fresh ginger, garlic, onions, yoghurt, curry leaves &amp; cumin</p></div>
  <div class="dish" style="--gap:14px"><div class="dish-row"><span class="dish-name">Karahi Paneer <span class="chilli amber" role="img" aria-label="mild chilli"></span><span class="badge">D</span></span><span class="price">€7.70</span></div><p class="dish-desc">A colourful curry prepared using homemade Indian cheese.</p></div>
  <div class="dish" style="--gap:14px"><div class="dish-row"><span class="dish-name">Paneer Jalfrezi <span class="chilli amber" role="img" aria-label="mild chilli"></span><span class="badge">D</span><span class="badge">N</span></span><span class="price">€8.00</span></div><p class="dish-desc">Cottage cheese &amp; peppers with roasted coriander seeds, onions and green chillies</p></div>
  <div class="dish" style="--gap:14px"><div class="dish-row"><span class="dish-name">Sambhar Vegetable Curry <span class="badge">LF</span></span><span class="price">€7.70</span></div><p class="dish-desc">Vegetable curry cooked with a lentils, curry leaves and mustard seeds</p></div>
  <div class="dish" style="--gap:14px"><div class="dish-row"><span class="dish-name">Aloo Saag Hariyali <span class="badge">D</span></span><span class="price">€7.70</span></div><p class="dish-desc">Pan fried potatoes &amp; spinach, flavoured with kasoori methi &amp; fresh coriander</p></div>
  <div class="dish"><div class="dish-row"><span class="dish-name">Vegetable Biryani <span class="badge">N</span></span><span class="price">€8.50</span></div><p class="dish-desc">Basmati rice cooked with vegetables, fresh herbs, spices and fried golden onions. Served with your choice of mixed vegetable sauce or raita.</p></div>
</section>

<section class="menu-section col-c side-list" style="top:802px">
  <h2 class="section-title two-line" style="margin-bottom:12px;width:200px">Naan Bread &amp; Side Orders <span class="emblem" role="img" aria-label="elephant emblem"></span></h2>
  <div class="dish"><div class="dish-row"><span class="dish-name">Naan <span class="badge">CL</span></span><span class="price">€1.90</span></div></div>
  <div class="dish"><div class="dish-row"><span class="dish-name">Garlic Naan <span class="badge">CL</span></span><span class="price">€2.50</span></div></div>
  <div class="dish"><div class="dish-row"><span class="dish-name">Garlic Chilli Naan <span class="badge">CL</span></span><span class="price">€3.00</span></div></div>
  <div class="dish"><div class="dish-row"><span class="dish-name">Peshawari Naan <span class="badge">CL</span></span><span class="price">€2.70</span></div></div>
  <div class="dish"><div class="dish-row"><span class="dish-name">Keema Naan <span class="badge">CL</span></span><span class="price">€3.00</span></div></div>
  <div class="dish"><div class="dish-row"><span class="dish-name">Coriander Naan <span class="badge">CL</span></span><span class="price">€2.50</span></div></div>
  <div class="dish"><div class="dish-row"><span class="dish-name">Blue Cheese Naan <span class="badge">CL</span></span><span class="price">€2.50</span></div></div>
  <div class="dish"><div class="dish-row"><span class="dish-name">G.O.C <span class="badge">CL</span></span><span class="price">€3.00</span></div></div>
  <div class="dish"><div class="dish-row"><span class="dish-name">Boiled Basmati</span><span class="price">€2.00</span></div></div>
  <div class="dish"><div class="dish-row"><span class="dish-name">Pilau Rice</span><span class="price">€2.10</span></div></div>
  <div class="dish"><div class="dish-row"><span class="dish-name">Vegetable &amp; Fruit Pilau</span><span class="price">€2.50</span></div></div>
  <div class="dish"><div class="dish-row"><span class="dish-name">Poppadums (2) &amp; Spiced Onions</span><span class="price">€2.00</span></div></div>
  <div class="dish"><div class="dish-row"><span class="dish-name">Onion, Mint &amp; Cucumber Raita <span class="badge">D</span></span><span class="price">€2.00</span></div></div>
  <div class="dish"><div class="dish-row"><span class="dish-name">Mixed Pickle Dips</span><span class="price">€2.00</span></div></div>
  <div class="dish"><div class="dish-row"><span class="dish-name">Bombay Aloo <span class="badge">LF</span></span><span class="price">€5.00</span></div></div>
  <div class="dish"><div class="dish-row"><span class="dish-name">Tarka Dal Lentil Curry <span class="badge">LF</span></span><span class="price">€4.50</span></div></div>
  <div class="dish"><div class="dish-row"><span class="dish-name">Spinach Saag &amp; Indian Cheese <span class="badge">D</span></span><span class="price">€5.00</span></div></div>
  <div class="dish"><div class="dish-row"><span class="dish-name">Aloo Gobi Side <span class="badge">LF</span></span><span class="price">€5.00</span></div></div>
  <div class="dish"><div class="dish-row"><span class="dish-name">Aloo Chole Masala Side <span class="badge">LF</span></span><span class="price">€5.00</span></div></div>
</section>

</body>
</html>
```